Tavorin Brand Household Liquids

We need a logo designed, as well as a design concept under the Tavorin brand for dishwashing liquid, liquid handwashing soap and toilet bowl cleanser.

The design concept should be fresh and clean looking using green and blue colors.

The packaging should be targeted to mothers and ladies of the house who do the grocery shopping. It should convey the message that this product will magically clean their hands/ laundry/ whatnots.

Target Market(s)

Middle class to low end market (B,C,D)

Colors
00a990
0592cd
a54499

Requirements
Must have
• Tavorin the "Wizard" who magically removes dust/ germs/ dirt/ bacteria
Nice to have
• A wizard cartoon image on the label
Should not have
• black colors

```html
<!DOCTYPE html>
<html lang="en">
<head>
<meta charset="utf-8">
<title>Tavorin Toilet Bowl Cleaner – Bottle Label</title>
<link rel="stylesheet" href="https://fonts.googleapis.com/css2?family=Fredoka:wght@600&family=Mystery+Quest&display=swap">
<style>
  :root {
    --canvas-bg: #ffffff;
    --bottle-blue: #8fd8f8;
    --bottle-outline: #2a4a6a;
    --cap-blue: #1f4fb0;
    --cap-shade: #3a6fd0;
    --band-purple: #6b2a8a;
    --text-purple: #6b2a8a;
    --star-yellow: #f7c318;
    --label-green: #3cb44a;
    --label-edge: #3a3f9a;
    --wizard-tone: #8a4fb0;
    --white: #ffffff;
  }
  html, body {
    margin: 0;
    padding: 0;
    overflow: hidden;
    background: var(--canvas-bg);
  }
  .canvas {
    width: 967px;
    height: 1200px;
    position: relative;
    overflow: hidden;
    background: var(--canvas-bg);
  }
  .bottle-art {
    display: block;
    width: 967px;
    height: 1200px;
  }
  .bottle-body { fill: var(--bottle-blue); stroke: var(--bottle-outline); stroke-width: 1.2; }
  .bottle-cap { fill: var(--cap-blue); }
  .bottle-cap-highlight { fill: var(--cap-shade); opacity: .6; }
  .claim-band { fill: var(--band-purple); }
  .claim-figure { font-family: "Fredoka", sans-serif; font-weight: 600; font-size: 48px; fill: var(--white); }
  .claim-word { font-family: "Fredoka", sans-serif; font-weight: 600; font-size: 24px; fill: var(--white); }
  .claim-star { fill: var(--star-yellow); }
  .wizard-slot { fill: var(--wizard-tone); opacity: .85; }
  .tagline { font-family: "Mystery Quest", cursive; font-size: 26px; fill: var(--text-purple); }
  .brand-name { font-family: "Mystery Quest", cursive; font-size: 92px; fill: var(--text-purple); }
  .product-type { font-family: "Mystery Quest", cursive; font-size: 26px; fill: var(--text-purple); }
</style>
</head>
<body>
<main class="canvas">
  <svg class="bottle-art" viewBox="0 0 900 1117" preserveAspectRatio="none" aria-label="Tavorin toilet bowl cleaner bottle">
    <defs>
      <radialGradient id="label-glow" cx="50%" cy="52%" r="62%">
        <stop offset="0%" stop-color="var(--label-green)"/>
        <stop offset="62%" stop-color="var(--label-green)"/>
        <stop offset="100%" stop-color="var(--label-edge)"/>
      </radialGradient>
    </defs>

    <g class="bottle">
      <path class="bottle-cap" d="M340,208 L348,160 C356,140 372,128 392,122 L420,112 L452,114 C466,122 470,140 466,160 L448,212 Z"/>
      <path class="bottle-cap-highlight" d="M395,130 L425,120 L440,125 L430,175 L400,190 Z"/>
      <path class="bottle-body" d="M340,205 L446,210 C440,240 438,262 452,286 L604,480 C612,495 612,520 612,560 L612,990 C612,1005 600,1010 585,1010 L305,1010 C290,1010 282,1000 282,985 L282,322 C282,302 290,290 300,276 Z"/>
    </g>

    <g class="claim">
      <path class="claim-band" d="M284,300 L455,289 L492,334 C420,344 350,360 283,380 Z"/>
      <text class="claim-figure" x="294" y="358" textLength="72" lengthAdjust="spacingAndGlyphs">0%</text>
      <text class="claim-word" x="370" y="366" transform="rotate(-10 370 366)" textLength="84" lengthAdjust="spacingAndGlyphs">Bleach</text>
      <polygon class="claim-star" points="398,300 402,310 413,310 404,317 408,328 398,321 388,328 392,317 383,310 394,310"/>
    </g>

    <path class="label-panel" fill="url(#label-glow)" d="M300,610 C320,578 420,570 560,578 C600,581 606,600 606,640 L606,960 C606,990 588,1000 560,1000 L330,1000 C305,1000 292,985 292,960 Z"/>

    <rect class="wizard-slot" x="300" y="420" width="145" height="150" rx="30" role="img" aria-label="Cartoon wizard mascot with pointed hat and sparkling wand, with golden stars and swirls"/>

    <text class="tagline" x="445" y="553" textLength="125" lengthAdjust="spacingAndGlyphs">It’s Magic!</text>

    <text class="brand-name" x="305" y="842" transform="rotate(-7 305 842)" textLength="278" lengthAdjust="spacingAndGlyphs">TAVORIN</text>
    <text class="product-type" x="372" y="882" transform="rotate(-10 372 882)" textLength="212" lengthAdjust="spacingAndGlyphs">Toliet Bowl Cleaner</text>
  </svg>
</main>
</body>
</html>
```